Business Card Design

i am looking a business card for a car rental company long with Taxi service also a logo.
Updates

what is the latest with my project

Industry/Entity Type

Business

Contact Information for Business Card

name of the Company is Brenmoor Auto Hire and Cab Services
Address: Kell Bay Village, St. Oriel's Parish Antigua
Tele# 558-2047/6194852-613-9075
Email: tolvipark@quenmail.net

Font styles to use
Script

```html
<!DOCTYPE html>
<html lang="en">
<head>
<meta charset="utf-8">
<title>Brenmoor Auto Hire and Cab Services – Business Card</title>
<link rel="stylesheet" href="https://fonts.googleapis.com/css2?family=Mulish:wght@700;800&family=Questrial&display=swap">
<style>
  :root {
    --ink: #2b2928;
    --sun: #ffee45;
    --paper: #ecedeb;
    --white: #ffffff;
  }
  * { margin: 0; padding: 0; box-sizing: border-box; }
  html, body {
    width: 1200px;
    height: 838px;
    overflow: hidden;
    background: var(--paper);
  }
  .card {
    position: absolute;
    left: 109px;
    top: 135px;
    width: 953px;
    height: 565px;
    background: var(--sun);
    overflow: hidden;
  }
  .card__band {
    position: absolute;
    left: 0;
    top: 0;
    width: 100%;
    height: 297px;
    background: var(--ink);
  }
  .brand {
    position: absolute;
    left: 31px;
    top: 72px;
    width: 344px;
    height: 344px;
    border-radius: 50%;
    background: linear-gradient(to bottom, var(--sun) 0, var(--sun) 225px, var(--ink) 225px, var(--ink) 100%);
  }
  .brand__name {
    position: absolute;
    left: 32px;
    top: 78px;
    width: 280px;
    text-align: center;
    font-family: "Mulish", sans-serif;
    font-weight: 800;
    font-size: 30px;
    line-height: 1.2;
    color: var(--ink);
  }
  .address {
    position: absolute;
    left: 463px;
    top: 151px;
    display: flex;
    align-items: center;
    gap: 18px;
    color: var(--white);
  }
  .address__text {
    font-family: "Mulish", sans-serif;
    font-weight: 700;
    font-size: 32px;
    line-height: 41px;
  }
  .contact {
    position: absolute;
    left: 317px;
    display: flex;
    align-items: center;
    gap: 20px;
    color: var(--ink);
  }
  .contact--phone { top: 418px; }
  .contact--email { top: 475px; }
  .contact__icon { width: 30px; flex: none; }
  .contact__phone {
    font-family: "Mulish", sans-serif;
    font-weight: 800;
    font-size: 34px;
    letter-spacing: 2.2px;
  }
  .contact__email {
    font-family: "Questrial", sans-serif;
    font-size: 31px;
    letter-spacing: 1px;
  }
</style>
</head>
<body>
  <div class="card">
    <div class="card__band"></div>

    <div class="brand">
      <p class="brand__name">Brenmoor Auto Hire and Cab Services</p>
    </div>

    <div class="address">
      <svg class="address__icon" width="34" height="30" viewBox="0 0 34 30" aria-hidden="true">
        <path d="M17 2 L32 12 H2 Z" fill="var(--white)"/>
        <rect x="4" y="14" width="26" height="14" fill="var(--white)"/>
        <rect x="8" y="17" width="7" height="7" fill="var(--ink)"/>
        <rect x="19" y="17" width="7" height="7" fill="var(--ink)"/>
      </svg>
      <p class="address__text">Kell Bay Village,<br>St. Oriel's Parish Antigua</p>
    </div>

    <div class="contact contact--phone">
      <svg class="contact__icon" height="36" viewBox="0 0 30 36" aria-hidden="true">
        <path d="M8 3 L13 11 L10 14 C11 19 14 24 18 27 L21 24 L27 30 L23 34 C13 32 4 20 3 8 Z" fill="none" stroke="var(--ink)" stroke-width="3" stroke-linejoin="round"/>
      </svg>
      <p class="contact__phone">558-2047/ 6194852-613-9075</p>
    </div>

    <div class="contact contact--email">
      <svg class="contact__icon" height="22" viewBox="0 0 30 22" aria-hidden="true">
        <rect x="1.5" y="1.5" width="27" height="19" fill="none" stroke="var(--ink)" stroke-width="2.5"/>
        <path d="M2 3 L15 13 L28 3 M2 20 L11 11 M28 20 L19 11" fill="none" stroke="var(--ink)" stroke-width="2.5"/>
      </svg>
      <p class="contact__email">tolvipark@quenmail.net</p>
    </div>
  </div>
</body>
</html>
```